Graphic Design For Website Banner + 4 Product Images - More Work To Follow

We are in the process of launching a new website. I need to design a banner for the homepage, as well as some graphics for my product images.

Please find attached -

1) My current logo.
2) Banner Sample + Product Image Sample - both of these are a screenshot from a common website that I like the design and style of.
3) Colour Scheme Sample 1 - saved image showing colour scheme for BrushOtter that I like.
4) Colour Scheme Sample 2 - Saved image showing colour scheme for Plivo that I like.
5) Sample 1-4 - These are colour palette samples I created online showing what I like.
6) 4 blank product images to show what is required in the design.

To summarise I'll like to create a banner design and product images similar to what's been attached and have a consistent colour theme throughout. I'm happy to adjust the colours in my logo to match the final designs.

To begin with I'll be requesting 1 banner design and 4 product images. I'll have more work for the successful designer.

Banner -
Size to be 950x300. To contain the following wording -
Quality Printing
Offset|Digital|Wideformat
Deal Direct & Save
Possibly include some product images like the sample banner attached.

Product Images -
Size to be 263x263
1) Business Cards
2) Folded Brochures
3) Flyers
4) Presentation Folders
I've attached blank sample images of all 4 for your reference.

Please feel free to ask any questions as I'm happy to give further direction.

Target Market(s)

We are a commercial Printer offering a range of printed products

Font styles to use
Serif
Sans Serif

Colors
34a6d7
33b8a4
3277b5
86cfc7
86cae7
85acd3
00a990
0393ce
0255a3

```html
<!DOCTYPE html>
<html lang="en">
<head>
<meta charset="utf-8">
<title>Tallow Press – Web Banner and Product Images</title>
<link rel="stylesheet" href="https://fonts.googleapis.com/css2?family=Fira+Sans+Condensed:wght@500&family=Source+Sans+3:wght@400;600;700&display=swap">
<style>
  :root{
    --teal:#00a990;
    --sky:#1a96d0;
    --sage:#8fbfb1;
    --mint:#62f4df;
    --blue:#0b8fd0;
    --brand:#2f94cf;
    --ink:#1b2a36;
    --frame:#6b2fd9;
    --box-line:#19b3a0;
    --box-line-soft:#86ece2;
    --paper:#ffffff;
    --deep:#2a79a0;
    --panel-light:#eaf2fb;
  }
  *{margin:0;padding:0;box-sizing:border-box}
  html,body{width:1200px;height:773px;overflow:hidden;background:#fff}
  body{position:relative;font-family:"Source Sans 3",Arial,sans-serif;color:var(--ink)}
  .defs{position:absolute;width:0;height:0}

  .section-title{position:absolute;left:0;width:1164px;top:34px;text-align:center;font-size:17px;font-weight:400;letter-spacing:.2px}

  .banner{position:absolute;left:156px;top:65px;width:890px;height:281px;overflow:hidden;
    background:linear-gradient(90deg,var(--panel-light) 0%,var(--panel-light) 42%,#cfe5f3 49%,#2aa5cb 60%,#0ba79b 84%,var(--teal) 100%);
    box-shadow:3px 5px 6px rgba(0,0,0,.35)}
  .brand-name{position:absolute;left:20px;top:26px;font-family:"Source Sans 3",Arial,sans-serif;font-weight:600;font-size:31px;line-height:1.02;color:var(--brand);letter-spacing:.5px}
  .tagline{position:absolute;left:7px;width:363px;height:37px;color:#fff;font-family:"Fira Sans Condensed",Arial,sans-serif;font-weight:500;font-size:23px;line-height:37px;padding-left:13px;letter-spacing:.3px;white-space:nowrap}
  .tagline.quality{top:146px;background:var(--teal)}
  .tagline.methods{top:192px;background:var(--sky)}
  .tagline.save{top:238px;background:var(--sage)}
  .banner-art{position:absolute;left:0;top:0}

  .product-label{position:absolute;top:453px;width:246px;text-align:center;font-size:10px;font-weight:600}
  .product-box{position:absolute;top:482px;width:246px;height:246px;border:1px solid var(--box-line);overflow:hidden;background:#fff}
  .product-box.soft{border-color:var(--box-line-soft)}
  .product-box svg{display:block}

  .frame{fill:none;stroke:var(--frame);stroke-width:1.4}
  .frame-label{fill:#fff;font-size:8px;font-weight:600;letter-spacing:.3px;text-anchor:middle}
  .mint{fill:var(--mint)}
  .blueband{fill:var(--blue)}
  .paper{fill:var(--paper)}
  .card-name{fill:var(--brand);font-weight:600}
  .card-head{fill:var(--ink);font-size:9.5px;font-weight:600}
  .card-info{fill:var(--ink);font-size:7.6px;font-weight:700;text-anchor:middle}
  .deep{fill:var(--deep)}
</style>
</head>
<body>

<svg class="defs" aria-hidden="true">
  <defs>
    <filter id="lift" x="-20%" y="-20%" width="150%" height="150%">
      <feDropShadow dx="4" dy="5" stdDeviation="3" flood-color="#000" flood-opacity=".35"/>
    </filter>
    <linearGradient id="flyerTop" x1="0" y1="0" x2="0" y2="1">
      <stop offset="0" style="stop-color:#ffffff"/><stop offset="1" style="stop-color:#c9d7ee"/>
    </linearGradient>
    <linearGradient id="flyerBody" x1="0" y1="0" x2="0" y2="1">
      <stop offset="0" style="stop-color:#e3ebf8"/><stop offset="1" style="stop-color:#3b69c2"/>
    </linearGradient>
    <linearGradient id="flyerBar" x1="0" y1="0" x2="1" y2="0">
      <stop offset="0" style="stop-color:#ffffff"/><stop offset="1" style="stop-color:#5a83cf"/>
    </linearGradient>
    <radialGradient id="bloom">
      <stop offset="0" style="stop-color:#f2b38e"/><stop offset=".6" style="stop-color:#e6a3c4"/><stop offset="1" style="stop-color:#c69ad8;stop-opacity:0"/>
    </radialGradient>
    <linearGradient id="coverTint" x1="0" y1="0" x2="0" y2="1">
      <stop offset="0" style="stop-color:#f3f8fd"/><stop offset=".5" style="stop-color:#cfe6f5"/><stop offset="1" style="stop-color:#1f6e98"/>
    </linearGradient>
    <linearGradient id="innerPanel" x1="0" y1="0" x2="1" y2="0">
      <stop offset="0" style="stop-color:#d6d9dc"/><stop offset="1" style="stop-color:#ffffff"/>
    </linearGradient>
    <linearGradient id="brochureArt" x1="0" y1="0" x2="1" y2="1">
      <stop offset="0" style="stop-color:#f4f7fc"/><stop offset="1" style="stop-color:#6f93c4"/>
    </linearGradient>
    <linearGradient id="brochureOpen" x1="0" y1="0" x2="1" y2="1">
      <stop offset="0" style="stop-color:#3d6fa6"/><stop offset=".45" style="stop-color:#b9cfe6"/><stop offset="1" style="stop-color:#6d93c2"/>
    </linearGradient>
    <linearGradient id="clips" x1="0" y1="0" x2="1" y2="0">
      <stop offset="0" style="stop-color:#b88fd8"/><stop offset=".5" style="stop-color:#e48fb0"/><stop offset="1" style="stop-color:#e9c07c"/>
    </linearGradient>
    <linearGradient id="clipsDark" x1="0" y1="0" x2="1" y2="0">
      <stop offset="0" style="stop-color:#1d6f86"/><stop offset="1" style="stop-color:#0f8a6c"/>
    </linearGradient>

    <symbol id="business-card" viewBox="0 0 246 246">
      <rect class="mint" x="0" y="14" width="238" height="138" filter="url(#lift)"/>
      <rect class="blueband" x="0" y="140" width="14" height="12"/>
      <text class="card-name" x="76" y="64" font-size="21">TALLOW</text>
      <text class="card-name" x="76" y="86" font-size="21">PRESS</text>
      <rect class="paper" x="12" y="110" width="234" height="126" filter="url(#lift)"/>
      <rect class="blueband" x="12" y="222" width="172" height="14"/>
      <polygon class="mint" points="136,172 246,146 246,236 172,236"/>
      <text class="card-head" x="176" y="135">Business Card</text>
      <text class="card-name" x="28" y="162" font-size="20">TALLOW</text>
      <text class="card-name" x="28" y="184" font-size="20">PRESS</text>
      <text class="card-info" x="203" y="184">Company: Northvane</text>
      <text class="card-info" x="203" y="196">Name: Milo Renner</text>
      <text class="card-info" x="203" y="208">Email: milo@nrvn.co</text>
      <text class="card-info" x="203" y="220">Phone: (555) 014 2280</text>
    </symbol>

    <symbol id="flyer" viewBox="0 0 246 246">
      <rect x="44" y="0" width="155" height="246" fill="url(#flyerTop)" filter="url(#lift)"/>
      <rect x="44" y="100" width="155" height="146" fill="url(#flyerBody)"/>
      <text class="card-name" x="52" y="28" font-size="15">TALLOW</text>
      <text class="card-name" x="52" y="44" font-size="15">PRESS</text>
      <rect x="48" y="104" width="120" height="9" fill="url(#flyerBar)"/>
      <rect x="48" y="119" width="120" height="9" fill="url(#flyerBar)"/>
      <rect x="48" y="134" width="120" height="9" fill="url(#flyerBar)"/>
      <rect x="178" y="100" width="3" height="146" fill="#4a7bd0"/>
      <rect x="187" y="100" width="3" height="146" fill="#4a7bd0"/>
      <rect x="194" y="100" width="2" height="146" fill="#ffffff" opacity=".7"/>
      <g role="img" aria-label="Watercolour flower illustration">
        <ellipse cx="103" cy="182" rx="46" ry="32" fill="url(#bloom)"/>
      </g>
    </symbol>

    <symbol id="folder" viewBox="0 0 246 246">
      <polygon points="143,10 206,4 206,208 143,216" fill="url(#innerPanel)" filter="url(#lift)"/>
      <polygon class="deep" points="143,126 206,120 206,208 143,216"/>
      <g role="img" aria-label="Pale blue botanical cover illustration">
        <polygon points="56,8 143,16 143,238 56,228" fill="url(#coverTint)" filter="url(#lift)"/>
      </g>
      <polygon class="deep" points="128,16 143,16 143,128 128,130" opacity=".85"/>
      <text class="card-name" x="64" y="42" font-size="13">TALLOW</text>
      <text class="card-name" x="64" y="57" font-size="13">PRESS</text>
    </symbol>

    <symbol id="brochure" viewBox="0 0 246 246">
      <polygon points="68,66 160,58 160,200 68,208" fill="#e6edf6" filter="url(#lift)"/>
      <g role="img" aria-label="Blue ink splash and leaf illustration">
        <polygon points="160,58 222,44 222,216 160,200" fill="url(#brochureOpen)" filter="url(#lift)"/>
        <polygon points="24,84 102,76 104,214 26,222" fill="url(#brochureArt)" filter="url(#lift)"/>
      </g>
      <rect x="110" y="84" width="40" height="3" fill="#7d8a96"/>
      <rect x="110" y="92" width="40" height="3" fill="#7d8a96"/>
      <rect x="110" y="100" width="40" height="3" fill="#7d8a96"/>
      <rect x="110" y="108" width="32" height="3" fill="#7d8a96"/>
      <text class="card-name" x="44" y="106" font-size="12">TALLOW</text>
      <text class="card-name" x="44" y="120" font-size="12">PRESS</text>
    </symbol>
  </defs>
</svg>

<h1 class="section-title">Web Banner</h1>

<section class="banner" aria-label="Homepage banner">
  <div class="brand-name">TALLOW<br>PRESS</div>
  <div class="tagline quality">QUALITY PRINTING</div>
  <div class="tagline methods">OFFSET | DIGITAL | WIDEFORMAT</div>
  <div class="tagline save">DEAL DIRECT &amp; SAVE</div>

  <svg class="banner-art" width="890" height="281" viewBox="0 0 890 281">
    <g role="img" aria-label="Row of pastel paper clips">
      <rect x="290" y="60" width="60" height="36" rx="10" fill="url(#clips)" opacity=".75"/>
    </g>
    <g role="img" aria-label="Row of dark green paper clips">
      <rect x="590" y="240" width="62" height="36" rx="10" fill="url(#clipsDark)" opacity=".7"/>
      <rect x="656" y="0" width="56" height="18" rx="6" fill="url(#clipsDark)" opacity=".6"/>
    </g>

    <use href="#business-card" x="409" y="15" width="93" height="93"/>
    <rect class="frame" x="391" y="12" width="130" height="95"/>
    <text class="frame-label" x="456" y="15">BUSINESS CARDS</text>

    <use href="#flyer" x="389" y="140" width="135" height="135"/>
    <rect class="frame" x="398" y="132" width="117" height="145"/>
    <text class="frame-label" x="456" y="135">FLYERS</text>

    <use href="#folder" x="552" y="72" width="143" height="143"/>
    <rect class="frame" x="561" y="60" width="130" height="157"/>
    <text class="frame-label" x="626" y="63">PRESENTATION FOLDERS</text>

    <use href="#business-card" x="757" y="15" width="93" height="93"/>
    <rect class="frame" x="729" y="12" width="151" height="95"/>
    <text class="frame-label" x="804" y="15">BUSINESS CARDS</text>

    <use href="#brochure" x="712" y="119" width="162" height="162"/>
    <rect class="frame" x="706" y="130" width="174" height="144"/>
    <text class="frame-label" x="793" y="133">FOLDED BROCHURES</text>
  </svg>
</section>

<div class="product-label" style="left:55px">Presentation Folders</div>
<div class="product-box" style="left:55px">
  <svg width="246" height="246" viewBox="0 0 246 246"><use href="#folder" width="246" height="246"/></svg>
</div>

<div class="product-label" style="left:322px">Business Cards</div>
<div class="product-box" style="left:322px">
  <svg width="246" height="246" viewBox="0 0 246 246"><use href="#business-card" width="246" height="246"/></svg>
</div>

<div class="product-label" style="left:600px">Flyers</div>
<div class="product-box soft" style="left:600px">
  <svg width="246" height="246" viewBox="0 0 246 246"><use href="#flyer" width="246" height="246"/></svg>
</div>

<div class="product-label" style="left:862px">Folded Brochures</div>
<div class="product-box soft" style="left:862px">
  <svg width="246" height="246" viewBox="0 0 246 246"><use href="#brochure" width="246" height="246"/></svg>
</div>

</body>
</html>
```